Velm Care Website Homepage & Template Design
Multiple Template Design
Velm Care Website Homepage & Template Design - Pharmacy/Pharmaceuticals
Creative Brief
Pharmacy/Pharmaceuticals
www.velmcare-example.com
Velm Care provides medications for patients taking Specialty medications & for Long-Term Care Facilities. We also provide services for our patients that go above the average pharmacy. Our business is mainly conducted through referrals and we are not a store-front/retail pharmacy.
We are patient and care focused and want to portray a caring feeling through our website.
LIKE: Clean and welcoming feel. Do not want the site to be too stark. * RSS Feed - twitter accounts * Java Script / J-query * Multiple Templates (3) * Search Capability * Top Navigation * Social Media Links DISLIKE - numbered java images, would prefer a small dot to manually flip between - too many colors - current right hand information block on our homepage & subsequent pages
Service Oriented
7475 pantone spot
185 process special mix
405 process special mix
http://www.brinsola-example.com/home.html
http://qpzpharmacy-example.com/
http://www.tolvexcare-example.com/tolvex/index.asp
Additional Website Reference: http://www.dunemedrx-example.com/2010/index.php - Must have multiple templates for varying pages (3) - Must include a homepage design Additional Colors from Standards: - 5503 Lite Blue Process

```html
<!DOCTYPE html>
<html lang="en">
<head>
<meta charset="utf-8">
<title>Velm Care – Pharmacy Homepage</title>
<link href="https://fonts.googleapis.com/css2?family=Arimo:wght@400;700&family=Noto+Serif:wght@400;700&display=swap" rel="stylesheet">
<style>
:root{
  --bg:#dde6e7;
  --bg-line:#d3dddf;
  --teal:#3f9aa0;
  --teal-dark:#2f7d83;
  --teal-text:#4aa0a6;
  --red:#d8353c;
  --grey:#666d70;
  --nav-top:#5b5f62;
  --nav-bottom:#232527;
  --panel:#eef3f3;
  --footer:#4e9ea3;
  --white:#ffffff;
}
*{margin:0;padding:0;box-sizing:border-box}
html,body{width:1200px;height:951px;overflow:hidden}
body{
  position:relative;
  font-family:"Arimo",Arial,sans-serif;
  background:repeating-linear-gradient(45deg,var(--bg) 0 3px,var(--bg-line) 3px 4px);
  color:var(--grey);
}
a{color:inherit;text-decoration:none}

/* header */
.brand{position:absolute;left:158px;top:22px;display:flex;align-items:center;gap:12px}
.brand-dot{width:34px;height:34px;border-radius:50%;background:var(--teal)}
.brand-name{font-size:44px;font-weight:700;color:var(--teal);letter-spacing:1px}
.share{position:absolute;left:820px;top:14px;display:flex;gap:8px}
.share span{width:40px;height:16px;background:#c9d3d5;border:1px solid #b7c2c4;border-radius:2px}
.util-links{position:absolute;right:156px;top:62px;display:flex;gap:10px;font-size:12px;color:var(--grey)}
.util-links span.sep{color:#aab}

/* nav */
.main-nav{
  position:absolute;left:158px;top:90px;width:886px;height:44px;border-radius:8px;
  background:linear-gradient(var(--nav-top),var(--nav-bottom));
  box-shadow:0 3px 6px rgba(0,0,0,.3);
  display:flex;align-items:center;padding-left:14px;
}
.main-nav a{font-family:"Noto Serif",Georgia,serif;font-size:15px;color:var(--white);padding:0 22px;height:30px;line-height:30px;border-radius:3px}
.main-nav a.active{background:linear-gradient(#7a7f83,#3d4043);box-shadow:inset 0 1px 0 rgba(255,255,255,.3)}
.search{position:absolute;right:14px;top:10px;display:flex;gap:6px}
.search input{width:172px;height:22px;border:none;border-radius:11px;background:var(--white)}
.search button{height:22px;padding:0 8px;border:1px solid #555;border-radius:3px;background:linear-gradient(#555,#222);color:var(--white);font:700 11px "Arimo",sans-serif}

/* slider */
.hero{
  position:absolute;left:164px;top:147px;width:874px;height:277px;
  background:linear-gradient(#f6f9f9,#dce9ea);border:4px solid var(--white);
  box-shadow:0 10px 14px -6px rgba(0,0,0,.35);overflow:hidden;
}
.hero-photo{position:absolute;left:0;top:0;width:470px;height:100%;
  background:linear-gradient(90deg,#cfe0e3 0%,#e9dccc 45%,#f1ece2 70%,rgba(241,245,245,0) 100%)}
.hero-title{position:absolute;left:457px;top:34px;font-family:"Noto Serif",Georgia,serif;font-size:26px;color:var(--teal-text)}
.hero-text{position:absolute;left:457px;top:80px;width:360px;font-size:11.5px;line-height:15px;color:var(--teal-text)}
.btn-red{position:absolute;left:705px;top:228px;width:98px;height:26px;border-radius:3px;background:linear-gradient(#e04a50,#b8242b);color:var(--white);font-size:13px;text-align:center;line-height:26px}
.hero-arrow{position:absolute;top:121px}
.hero-arrow.prev{left:20px}.hero-arrow.next{right:20px}

/* news */
.news{position:absolute;left:164px;top:450px;width:874px;height:28px;border-top:1px dashed #b8c4c6;border-bottom:1px dashed #b8c4c6;text-align:center;line-height:26px;font-size:14px;color:var(--teal-text)}
.news b{font-family:"Noto Serif",Georgia,serif;color:var(--grey);font-weight:400;font-size:16px;margin-right:6px}

/* welcome */
.welcome{position:absolute;left:158px;top:500px;width:886px;border-bottom:2px solid #c5d0d2;padding-bottom:6px;font-family:"Noto Serif",Georgia,serif;font-size:22px;font-weight:700;color:var(--teal-dark)}
.welcome em{font-style:normal;color:var(--red)}
.welcome-photo{position:absolute;left:164px;top:542px;width:252px;height:132px;border:3px solid var(--white);box-shadow:0 3px 6px rgba(0,0,0,.25);background:linear-gradient(120deg,#bcd8e6,#e8edf0 55%,#9fc4d4)}
.welcome-text{position:absolute;left:437px;top:540px;width:606px;font-size:11px;line-height:14.5px;color:var(--teal-text)}
.welcome-text p+p{margin-top:2px}

/* service cards */
.card{position:absolute;top:699px;width:278px;height:150px;border-radius:6px;background:var(--panel);border:1px solid #cbd6d8;box-shadow:0 4px 8px rgba(0,0,0,.2)}
.card h3{position:absolute;left:20px;top:12px;font-family:"Noto Serif",Georgia,serif;font-weight:400;font-size:17px;color:var(--teal-dark);border-bottom:1px solid #c5d0d2;width:238px;padding-bottom:5px}
.card h3 em{font-style:normal;color:var(--red)}
.card .thumb{position:absolute;left:22px;top:56px;width:80px;height:60px;border:2px solid var(--white);box-shadow:0 2px 4px rgba(0,0,0,.25)}
.card p{position:absolute;left:118px;top:56px;width:140px;font-size:11px;line-height:14px;color:var(--teal-text)}
.card .more{position:absolute;right:18px;bottom:14px;width:54px;height:18px;border-radius:3px;background:linear-gradient(#4a4e51,#1f2123);color:var(--white);font-size:11px;font-weight:700;line-height:18px;padding-left:8px}
.card .more::after{content:"";position:absolute;right:4px;top:3px;width:12px;height:12px;border-radius:50%;background:var(--teal)}

/* footer */
.site-footer{position:absolute;left:0;top:869px;width:1200px;height:82px;background:var(--footer)}
.footer-links{position:absolute;left:158px;top:20px;display:flex;gap:12px;font-size:12px;color:var(--white)}
.copyright{position:absolute;left:158px;top:50px;font-size:11px;color:var(--white)}
.social{position:absolute;right:158px;top:18px;display:flex;gap:8px}
.social span{width:22px;height:22px;border-radius:4px;background:#eaf3f4}
</style>
</head>
<body>

<header>
  <div class="brand"><span class="brand-dot"></span><span class="brand-name">VELM CARE</span></div>
  <div class="share"><span></span><span></span><span></span></div>
  <nav class="util-links">
    <a href="#">Careers</a><span class="sep">|</span><a href="#">Philanthropy</a><span class="sep">|</span><a href="#">Contact Us</a><span class="sep">|</span><a href="#">Login</a><span class="sep">|</span><a href="#">Register</a>
  </nav>
  <nav class="main-nav">
    <a href="#" class="active">Home</a><a href="#">About Us</a><a href="#">For Patients</a><a href="#">For Physicians</a><a href="#">For Partners</a>
    <form class="search"><input type="text" aria-label="Search"><button type="button">SEARCH</button></form>
  </nav>
</header>

<section class="hero">
  <div class="hero-photo" role="img" aria-label="Photo of a joyful woman with arms raised in a bright open setting"></div>
  <h2 class="hero-title">Velm Care</h2>
  <p class="hero-text">Lorem Ipsum is simply dummy text of the printing and typesetting industry. Lorem Ipsum has been the industry's standard dummy text ever since the 1500s, when an unknown printer took a galley of type and scrambled it to make a type specimen book.<br>It has survived not only five centuries, but also the leap into electronic typesetting,<br>remaining essentially unchanged. It was popularised in the 1960s with the release.</p>
  <a href="#" class="btn-red">Lern More</a>
  <svg class="hero-arrow prev" width="34" height="34" viewBox="0 0 34 34"><circle cx="17" cy="17" r="16" fill="#3f9aa0"/><path d="M20 10l-7 7 7 7" stroke="#fff" stroke-width="3" fill="none"/></svg>
  <svg class="hero-arrow next" width="34" height="34" viewBox="0 0 34 34"><circle cx="17" cy="17" r="16" fill="#3f9aa0"/><path d="M14 10l7 7-7 7" stroke="#fff" stroke-width="3" fill="none"/></svg>
</section>

<div class="news"><b>News :</b> Lorem Ipsum is simply dummy text of the printing and typesetting industry. Lorem Ipsum has been the industry's.</div>

<h1 class="welcome">Welcome To <em>VELM CARE</em>..!</h1>
<div class="welcome-photo" role="img" aria-label="Photo of a smiling nurse in scrubs"></div>
<div class="welcome-text">
  <p>Lorem Ipsum is simply dummy text of the printing and typesetting industry. Lorem Ipsum has been the industry's standard dummy text ever since the 1500s, when an unknown printer took a galley of type and scrambled it to make a type specimen book. It has survived not only five centuries, but also the leap into electronic typesetting, remaining essentially unchanged. It was popularised in the 1960s with the release of Letraset sheets containing Lorem Ipsum passages, and more recently with desktop publishing software like Aldus PageMaker including versions of Lorem Ipsum.</p>
  <p>Lorem Ipsum is simply dummy text of the printing and typesetting industry. Lorem Ipsum has been the industry's standard dummy text ever since the 1500s.</p>
</div>

<article class="card" style="left:159px">
  <h3><em>Treatment</em> Programs</h3>
  <div class="thumb" role="img" aria-label="Photo of a caregiver with a patient" style="background:linear-gradient(135deg,#d9c4b0,#8fb5c2)"></div>
  <p>Lorem Ipsum the printing and typesetting Ipsum has been the industries standard</p>
  <a href="#" class="more">More</a>
</article>
<article class="card" style="left:462px">
  <h3><em>Infusion</em> Therapy</h3>
  <div class="thumb" role="img" aria-label="Photo of a nurse giving infusion care" style="background:linear-gradient(135deg,#e2cbb8,#b79e8c)"></div>
  <p>Lorem Ipsum the printing and typesetting Ipsum has been the industries standard</p>
  <a href="#" class="more">More</a>
</article>
<article class="card" style="left:763px">
  <h3><em>Home</em> Health</h3>
  <div class="thumb" role="img" aria-label="Photo of a home health visit" style="background:linear-gradient(135deg,#cfb7a4,#e6ddd2)"></div>
  <p>Lorem Ipsum the printing and typesetting Ipsum has been the industries standard</p>
  <a href="#" class="more">More</a>
</article>

<footer class="site-footer">
  <nav class="footer-links">
    <a href="#">Home</a><span>|</span><a href="#">About Us</a><span>|</span><a href="#">For Patients</a><span>|</span><a href="#">For Physicians</a><span>|</span><a href="#">For Partners</a><span>|</span><a href="#">Careers</a><span>|</span><a href="#">Philanthropy</a><span>|</span><a href="#">Contact Us</a>
  </nav>
  <p class="copyright">Copyright © 2012 www.velmcare-example.com</p>
  <div class="social"><span></span><span></span><span></span><span></span></div>
</footer>

</body>
</html>
```